Web Design for Independent Pet Supply shop.

Larkfield Critter Depot is a locally owned and operated premium natural pet food store and supply company with 2 thriving retail stores in Bend, Oregon, and a home delivery service. The pet food offered is the best on the market and may be described as “holistic”. Also on offer is a vast selection of toys, training tools, treats, and other supplies, as well as dog washing services that range from "do-it yourself" to "spa." Current site: LarkfieldCritterDepot.com. They need a new, updated and responsive site.
Likes:
Tovmira.com: Natural colors, not loud, pages in motion, simple & clean but very informative.
Dunmoregale.com: Everything in simple big colorful blocks. The specials run across the top and in motion. This site looks very professional but simple. The information is available several different places.
Quillbarrow.com: Again big blocks through out. Very Fun and inviting. Tons of information with videos and recipes and testimonials. Pleasant feel and colors as well.
Dislikes:
Zinvor.com: Looks cheap, hate the colors, very busy and over whelming. Hate the old style header bar going across with options. Too many printed words instead of fun images.
Colors should be "natural" tones, warm and soothing. Deep dark blue and greys with earthy wood color.
Do Not Use: Blue violet, violet, red violet

```html
<!DOCTYPE html>
<html lang="en">
<head>
<meta charset="utf-8">
<title>Larkfield Critter Depot</title>
<link rel="stylesheet" href="https://fonts.googleapis.com/css2?family=Montserrat:wght@500;600;700&family=Questrial&family=Open+Sans:wght@400;600;700&display=swap">
<style>
:root{
  --wood:#b07c3c;
  --wood-light:#c99a5b;
  --wood-dark:#8e5f2a;
  --rust:#c0672e;
  --ink:#2a2a2a;
  --nav:#2b2b2b;
  --band:#262626;
  --paper:#fafafa;
  --news-bg:#e1e1e1;
  --footer:#272727;
  --white:#ffffff;
}
*{margin:0;padding:0;box-sizing:border-box}
html,body{width:1200px;height:2535px;overflow:hidden}
body{position:relative;background:var(--white);font-family:"Questrial",sans-serif;color:var(--ink)}
.abs{position:absolute}

/* header */
.site-header{left:0;top:0;width:1200px;height:82px;background:var(--white)}
.brand{display:flex;align-items:center;gap:10px;font-family:"Montserrat",sans-serif;font-weight:700;color:var(--wood);white-space:nowrap}
.brand-dot{border-radius:50%;background:var(--wood);flex:none}
.site-header .brand{left:200px;top:22px;font-size:20px}
.site-header .brand-dot{width:34px;height:34px}
.contact-social{right:193px;top:6px;display:flex;gap:8px}
.social-square{width:27px;height:27px;background:var(--wood);border-radius:2px}
.contact-line{right:193px;font-size:11.5px;color:#555;text-align:right;font-family:"Open Sans",sans-serif;white-space:nowrap}

/* nav */
.main-nav{left:0;top:82px;width:1200px;height:67px;background:var(--nav)}
.nav-item{position:absolute;top:19px;height:31px;line-height:31px;font-size:13.5px;color:#e8e8e8;transform:translateX(-50%);padding:0 10px;white-space:nowrap;font-family:"Open Sans",sans-serif}
.nav-item.is-active{width:88px;text-align:center;background:var(--wood);color:var(--white)}

/* hero */
.hero{left:0;top:149px;width:1200px;height:494px;background:linear-gradient(100deg,#2d2a1f 0%,#a8612a 18%,#d98a3c 38%,#b86a2c 55%,#3a3028 70%,#d9a98e 82%,#7a5a48 100%)}
.slider-controls{left:498px;top:588px;display:flex;align-items:center;gap:14px}
.slider-arrow{width:14px;height:22px}
.slider-dot{width:13px;height:13px;border-radius:50%;background:#1f2a3a}
.slider-dot.is-current{background:#8a6a4a}

/* tagline */
.tagline-band{left:0;top:643px;width:1200px;height:92px;background:var(--band)}
.tagline{left:220px;top:34px;width:540px;white-space:nowrap;font-family:"Montserrat",sans-serif;font-weight:600;font-size:19px;letter-spacing:-0.2px;color:var(--white)}
.quote-button{left:840px;top:26px;width:135px;height:39px;line-height:39px;text-align:center;background:linear-gradient(var(--wood-light),var(--wood-dark));color:var(--white);font-family:"Open Sans",sans-serif;font-weight:700;font-size:13px;box-shadow:0 0 0 1px #d9b37e inset}

/* features */
.features{left:0;top:735px;width:1200px;height:457px;background:var(--paper)}
.feature{position:absolute;top:73px;width:230px;transform:translateX(-50%);text-align:center}
.feature-photo{width:169px;height:169px;border-radius:50%;margin:0 auto}
.feature-text{margin-top:33px;font-size:15.5px;line-height:19px;color:#333;font-family:"Open Sans",sans-serif}
.read-more{display:inline-block;width:84px;height:27px;line-height:27px;margin-top:17px;background:var(--ink);color:var(--white);font-size:9px;font-weight:700;font-family:"Open Sans",sans-serif}
.read-more.is-wood{background:var(--wood)}

/* companions */
.companions{left:0;top:1192px;width:1200px;height:801px;background:radial-gradient(ellipse at 30% 30%,#3c3c3c,#2e2e2e 60%,#292929)}
.section-rule{position:absolute;height:1px;background:#8a8a8a}
.companions-title{left:0;width:1200px;top:42px;text-align:center;font-size:33px;font-weight:400;color:var(--white);font-family:"Questrial",sans-serif}
.companions-sub{left:0;width:1200px;top:90px;text-align:center;font-size:14.5px;color:var(--white);font-family:"Open Sans",sans-serif;font-weight:600}
.companion-tile{position:absolute;width:267px;height:270px}
.companion-tile.is-selected{border:3px solid #111;outline:2px solid #ddd;outline-offset:-5px}

/* news */
.news{left:0;top:1993px;width:1200px;height:347px;background:var(--news-bg)}
.news-title{left:0;width:1200px;top:26px;text-align:center;font-family:"Montserrat",sans-serif;font-weight:500;font-size:26px;color:#222}
.news .section-rule{background:#555}
.news-card{position:absolute;top:93px;width:411px;height:182px;background:var(--white)}
.news-photo{position:absolute;left:0;top:0;width:192px;height:182px;background:linear-gradient(160deg,#9fb6a4 0%,#d8d4cc 35%,#2f4f9c 65%,#1e2c55 100%)}
.news-body{position:absolute;left:222px;top:30px;width:170px}
.news-heading{font-family:"Open Sans",sans-serif;font-weight:700;font-size:14.5px;color:#222}
.news-copy{margin-top:12px;font-size:8.2px;line-height:10.5px;color:#555;font-family:"Open Sans",sans-serif}
.news-button{display:block;width:69px;height:22px;line-height:22px;margin-top:14px;text-align:center;background:var(--rust);color:var(--white);font-size:8.5px;font-family:"Open Sans",sans-serif}

/* footer */
.site-footer{left:0;top:2340px;width:1200px;height:195px;background:var(--footer)}
.site-footer .brand{left:203px;top:86px;font-size:17px}
.site-footer .brand-dot{width:30px;height:30px}
.footer-heading{font-family:"Montserrat",sans-serif;font-weight:700;font-size:15.5px;color:var(--white)}
.footer-links{list-style:none;font-size:12.5px;line-height:18.6px;color:#e6e6e6;font-family:"Open Sans",sans-serif}
.footer-social{display:flex;gap:11px}
.footer-social .social-square{width:30px;height:30px}
.subscribe-field{width:192px;height:27px;background:var(--white);font-size:9.5px;line-height:27px;padding-left:7px;color:#444;font-family:"Open Sans",sans-serif}
</style>
</head>
<body>

<header class="site-header abs">
  <div class="brand abs"><span class="brand-dot"></span>Larkfield Critter Depot</div>
  <div class="contact-social abs" aria-label="Social links">
    <span class="social-square"></span><span class="social-square"></span><span class="social-square"></span><span class="social-square"></span><span class="social-square"></span>
  </div>
  <p class="contact-line abs" style="top:36px">Call Us : 555-014-2770</p>
  <p class="contact-line abs" style="top:53px">Or Email Us : larkfieldcritterdepot.com</p>
</header>

<nav class="main-nav abs">
  <span class="nav-item is-active" style="left:232px">Home</span>
  <span class="nav-item" style="left:331px">Events</span>
  <span class="nav-item" style="left:421px">Blog</span>
  <span class="nav-item" style="left:515px">About</span>
  <span class="nav-item" style="left:612px">Dog Wash</span>
  <span class="nav-item" style="left:705px">Products</span>
  <span class="nav-item" style="left:796px">Links</span>
  <span class="nav-item" style="left:896px">Contact</span>
  <span class="nav-item" style="left:989px">Resources</span>
</nav>

<section class="hero abs" role="img" aria-label="Golden retriever close-up beside a smiling woman"></section>
<div class="slider-controls abs">
  <svg class="slider-arrow" viewBox="0 0 14 22"><path d="M11 2 3 11l8 9" fill="none" stroke="#1f2a3a" stroke-width="4"/></svg>
  <span class="slider-dot is-current"></span><span class="slider-dot"></span><span class="slider-dot"></span><span class="slider-dot"></span>
  <svg class="slider-arrow" viewBox="0 0 14 22"><path d="M3 2l8 9-8 9" fill="none" stroke="#1f2a3a" stroke-width="4"/></svg>
</div>

<section class="tagline-band abs">
  <h1 class="tagline abs">DEDICATED TO A BETTER DIET FOR A HEALTHIER PET</h1>
  <span class="quote-button abs">Get Your Quote</span>
</section>

<section class="features abs">
  <div class="feature" style="left:264px">
    <div class="feature-photo" role="img" aria-label="Alert terrier mix in profile on grass" style="background:radial-gradient(circle,#c89a6a,#5f7a3c 75%)"></div>
    <p class="feature-text">ipsum dolor sit amet,<br>consectetur dipisicing elit,<br>sed do eiusmod tempor</p>
    <span class="read-more is-wood">Read more</span>
  </div>
  <div class="feature" style="left:487px">
    <div class="feature-photo" role="img" aria-label="Golden puppy sitting on grass" style="background:radial-gradient(circle,#e6c07e,#4f8a2c 75%)"></div>
    <p class="feature-text">ipsum dolor sit amet,<br>consectetur dipisicing elit,<br>sed do eiusmod tempor</p>
    <span class="read-more">Read more</span>
  </div>
  <div class="feature" style="left:712px">
    <div class="feature-photo" role="img" aria-label="White puppy against green background" style="background:radial-gradient(circle,#f1f0e6,#dcdccc 45%,#6e9a3a 85%)"></div>
    <p class="feature-text">ipsum dolor sit amet,<br>consectetur dipisicing elit,<br>sed do eiusmod tempor</p>
    <span class="read-more">Read more</span>
  </div>
  <div class="feature" style="left:935px">
    <div class="feature-photo" role="img" aria-label="Brown puppy sleeping on a white blanket" style="background:radial-gradient(circle at 50% 40%,#b86a2e,#d9a070 55%,#eee 85%)"></div>
    <p class="feature-text">ipsum dolor sit amet,<br>consectetur dipisicing elit,<br>sed do eiusmod tempor</p>
    <span class="read-more">Read more</span>
  </div>
</section>

<section class="companions abs" role="img" aria-label="Faint background photo of people with a dog">
  <span class="section-rule" style="left:186px;top:65px;width:119px"></span>
  <span class="section-rule" style="left:913px;top:65px;width:101px"></span>
  <h2 class="companions-title abs">Are you looking for a new campanion?</h2>
  <p class="companions-sub abs">ipsum dolor sit amet, consectetur dipisicing elit, sed do eiusmod tempor</p>
  <div class="companion-tile is-selected" role="img" aria-label="Brown puppy sleeping on a white blanket" style="left:177px;top:148px;background:linear-gradient(160deg,#eee 0%,#c57a38 40%,#a85c24 60%,#f2f2f2 85%)"></div>
  <div class="companion-tile" role="img" aria-label="White puppy against green background" style="left:468px;top:148px;background:linear-gradient(90deg,#4f8a8a 0%,#eceadc 30%,#f4f2ea 60%,#7aa040 100%)"></div>
  <div class="companion-tile" role="img" aria-label="Two golden puppies in colourful buckets" style="left:759px;top:148px;background:linear-gradient(180deg,#5d8a2c 0%,#e3c58a 35%,#d8b878 60%,#4aa0d0 85%,#c080b0 100%)"></div>
  <div class="companion-tile" role="img" aria-label="Brown puppy sleeping on a white blanket" style="left:177px;top:441px;background:linear-gradient(160deg,#eee 0%,#c57a38 40%,#a85c24 60%,#f2f2f2 85%)"></div>
  <div class="companion-tile" role="img" aria-label="White puppy against green background" style="left:468px;top:441px;background:linear-gradient(90deg,#4f8a8a 0%,#eceadc 30%,#f4f2ea 60%,#7aa040 100%)"></div>
  <div class="companion-tile" role="img" aria-label="Two golden puppies in colourful buckets" style="left:759px;top:441px;background:linear-gradient(180deg,#5d8a2c 0%,#e3c58a 35%,#d8b878 60%,#4aa0d0 85%,#c080b0 100%)"></div>
</section>

<section class="news abs">
  <span class="section-rule" style="left:186px;top:45px;width:296px"></span>
  <span class="section-rule" style="left:716px;top:45px;width:298px"></span>
  <h2 class="news-title abs">News &amp; Events</h2>
  <article class="news-card" style="left:176px">
    <div class="news-photo" role="img" aria-label="Group of people seated at an event"></div>
    <div class="news-body">
      <h3 class="news-heading">Ipsum dolor sit amet,</h3>
      <p class="news-copy">Lorem ipsum dolor sit amet, consectetur adipiscing elit, sed do eiusmod tempor incididunt ut labore et dolore magna aliqua ut enim ad minim veniam quis nostrud exercitation ullamco laboris nisi.</p>
      <span class="news-button">Read more</span>
    </div>
  </article>
  <article class="news-card" style="left:615px">
    <div class="news-photo" role="img" aria-label="Group of people seated at an event"></div>
    <div class="news-body">
      <h3 class="news-heading">Ipsum dolor sit amet,</h3>
      <p class="news-copy">Lorem ipsum dolor sit amet, consectetur adipiscing elit, sed do eiusmod tempor incididunt ut labore et dolore magna aliqua ut enim ad minim veniam quis nostrud exercitation ullamco laboris nisi.</p>
      <span class="news-button">Read more</span>
    </div>
  </article>
</section>

<footer class="site-footer abs">
  <div class="brand abs"><span class="brand-dot"></span>Larkfield Critter Depot</div>
  <h4 class="footer-heading abs" style="left:488px;top:41px">COMPANY</h4>
  <ul class="footer-links abs" style="left:488px;top:68px">
    <li>Home</li><li>Events</li><li>Blog</li><li>About</li><li>Dog Wash</li>
  </ul>
  <ul class="footer-links abs" style="left:664px;top:68px">
    <li>Resources</li><li>Products</li><li>Contact</li><li>Link</li>
  </ul>
  <h4 class="footer-heading abs" style="left:804px;top:41px">Follow Us</h4>
  <div class="footer-social abs" style="left:806px;top:75px">
    <span class="social-square"></span><span class="social-square"></span><span class="social-square"></span><span class="social-square"></span><span class="social-square"></span>
  </div>
  <div class="subscribe-field abs" style="left:808px;top:122px">Enter your email to subscribe</div>
</footer>

</body>
</html>
```